Vantorel Business Card

I want a business card for me and my employees.
On one side it must be in Greek and on the other side in English. The color must much the one of the logo

Target Market(s)

Customers that are looking for security and antipiracy advisors

Contact Information for Business Card

Title, Email, Phone, website , Mobile Address Zip code, city and country

Requirements
Must have
• The colors of our logo (the blue ones)

```html
<!DOCTYPE html>
<html lang="en">
<head>
<meta charset="utf-8">
<title>Vantorel Advisory – Business Cards</title>
<link rel="stylesheet" href="https://fonts.googleapis.com/css2?family=Noto+Sans:wght@400;500;700&display=swap">
<style>
  :root {
    --page-bg: #d4d5d7;
    --card-navy-dark: #212050;
    --card-navy-light: #2a2968;
    --ink: #ffffff;
    --ink-soft: #e6e6f2;
  }
  * { margin: 0; padding: 0; box-sizing: border-box; }
  html, body {
    width: 900px; height: 1200px; overflow: hidden;
    background: var(--page-bg);
    font-family: "Noto Sans", Arial, sans-serif;
  }
  .canvas { position: relative; width: 900px; height: 1200px; }
  .card {
    position: absolute; left: 149px; width: 602px; height: 387px;
    background: linear-gradient(135deg, var(--card-navy-dark) 0%, var(--card-navy-light) 100%);
    color: var(--ink);
  }
  .card--english { top: 200px; }
  .card--greek { top: 613px; }

  .brand {
    position: absolute; left: 331px; top: 50px;
    display: flex; align-items: center; gap: 12px;
    font-weight: 500; color: var(--ink);
  }
  .brand-square { width: 52px; height: 52px; border: 3px solid var(--ink); }
  .brand-name { display: flex; flex-direction: column; line-height: 1; }
  .brand-name .primary { font-size: 36px; letter-spacing: 0.5px; }
  .brand-name .secondary { font-size: 24px; letter-spacing: 2.6px; margin-top: 6px; }

  .holder { position: absolute; left: 48px; top: 198px; }
  .holder-name { font-size: 24px; font-weight: 700; line-height: 1.1; }
  .holder-title { font-size: 14px; font-weight: 400; color: var(--ink-soft); margin-top: 4px; }

  .contact-list {
    position: absolute; left: 48px; top: 272px; list-style: none;
    font-size: 14.5px; letter-spacing: 0.6px; color: var(--ink-soft);
  }
  .contact-list li { display: flex; align-items: center; height: 22.5px; }
  .contact-list svg { width: 13px; height: 13px; margin-right: 10px; fill: var(--ink); }

  .divider {
    position: absolute; left: 316px; top: 300px; width: 2px; height: 36px;
    background: var(--ink);
  }
  .address {
    position: absolute; left: 336px; top: 295px;
    font-size: 14.5px; line-height: 22.5px; letter-spacing: 0.3px; color: var(--ink-soft);
    font-style: normal;
  }
</style>
</head>
<body>
<main class="canvas">

  <section class="card card--english" lang="en">
    <div class="brand">
      <span class="brand-square"></span>
      <span class="brand-name"><span class="primary">VANTOREL</span><span class="secondary">ADVISORY</span></span>
    </div>
    <div class="holder">
      <h1 class="holder-name">Daniel Harrow</h1>
      <p class="holder-title">Director</p>
    </div>
    <ul class="contact-list">
      <li><svg viewBox="0 0 24 24"><path d="M6.6 10.8a15.1 15.1 0 0 0 6.6 6.6l2.2-2.2c.3-.3.7-.4 1-.2 1.1.4 2.3.6 3.6.6.6 0 1 .4 1 1V20c0 .6-.4 1-1 1A17 17 0 0 1 3 4c0-.6.4-1 1-1h3.5c.6 0 1 .4 1 1 0 1.3.2 2.5.6 3.6.1.3 0 .7-.2 1z"/></svg>07700900418</li>
      <li><svg viewBox="0 0 24 24"><path d="M2 5h20v14H2z M3.5 6.5 12 13l8.5-6.5" stroke="#2a2968" stroke-width="1.6"/></svg>daniel@vantoreladvisory.co.uk</li>
      <li><svg viewBox="0 0 24 24"><circle cx="12" cy="12" r="10"/><path d="M2 12h20M12 2v20M5 6.5h14M5 17.5h14M12 2c-3.5 3-3.5 17 0 20M12 2c3.5 3 3.5 17 0 20" stroke="#2a2968" stroke-width="1.2" fill="none"/></svg>www.vantorelconsulting.co.uk</li>
    </ul>
    <span class="divider"></span>
    <address class="address">48 Alderby Rd, Kelmore,<br>Bristol BS7 2QP, UK</address>
  </section>

  <section class="card card--greek" lang="el">
    <div class="brand">
      <span class="brand-square"></span>
      <span class="brand-name"><span class="primary">VANTOREL</span><span class="secondary">ADVISORY</span></span>
    </div>
    <div class="holder">
      <h1 class="holder-name">Ντάνιελ Χάροου</h1>
      <p class="holder-title">Σκηνοθέτης</p>
    </div>
    <ul class="contact-list">
      <li><svg viewBox="0 0 24 24"><path d="M6.6 10.8a15.1 15.1 0 0 0 6.6 6.6l2.2-2.2c.3-.3.7-.4 1-.2 1.1.4 2.3.6 3.6.6.6 0 1 .4 1 1V20c0 .6-.4 1-1 1A17 17 0 0 1 3 4c0-.6.4-1 1-1h3.5c.6 0 1 .4 1 1 0 1.3.2 2.5.6 3.6.1.3 0 .7-.2 1z"/></svg>07700900418</li>
      <li><svg viewBox="0 0 24 24"><path d="M2 5h20v14H2z M3.5 6.5 12 13l8.5-6.5" stroke="#2a2968" stroke-width="1.6"/></svg>daniel@vantoreladvisory.co.uk</li>
      <li><svg viewBox="0 0 24 24"><circle cx="12" cy="12" r="10"/><path d="M2 12h20M12 2v20M5 6.5h14M5 17.5h14M12 2c-3.5 3-3.5 17 0 20M12 2c3.5 3 3.5 17 0 20" stroke="#2a2968" stroke-width="1.2" fill="none"/></svg>www.vantorelconsulting.co.uk</li>
    </ul>
    <span class="divider"></span>
    <address class="address">48 Alderby Rd, Kelmore,<br>Bristol BS7 2QP, UK</address>
  </section>

</main>
</body>
</html>
```